NEW Website DESIGN for Glass & Solid Surfaces Company

Brand New website, contemporary, clean, visual (images), not busy. ATTACHED IS OUR LOG THAT YOU MUST USE.

The company is called Brightwell Panes & Stoneworks (BrightwellPS)
www.brightwellps.com
The website should be www.brightwellpns.com
one page for glass one page for solid surfaces www.brightwellpanesplashes.co.uk
www.brightwellstoneworkss.co.uk

Target Market(s)

Hotels, Commercial projects, Small focus on residential

Industry/Entity Type

Construction

Number of Pages Required

5+ page

Font styles to use
Sans Serif

Requirements
Must have
• COLOURS AS PER OUR LOGO - WHITE/YELLOW/GREY - WHITE BACK GROUND
• CLEAR SIMPLE NAVIGATION - MODER CLEAN CUT - DESIGN FEEL
• LATEST NAVIGATION FOR IMAGES and text to include per project details
• WORK/PROJECT AREA - NEWS AREA - TEAM AREA/ABOUT US/CONTACT US
• NEW PAGEwww.brightwellpanesplashes.co.uk - NEW PAGE www.brightwellstoneworkss.co.uk
• PLEASE COPY THIS TYPE OF TEMPALTE
• https://www.harlowmead.co.uk/project/grand-halls/
• MOBILE READY
• WORDPRESS
• MODERN IMAGES INCLUDING VELMARA KESTRIN AND GLASS PROJECTS
Nice to have
• NEW DESIGN MODER FRESH
• WEBSITES I LIKE THE TEMPLATE SHOULD BE LIKE THE WEBSITE BELOW
• https://www.harlowmead.co.uk/
Should not have
• NOT Old fashion template, not busy NAVIGATION
• NO BLACK
• NO DARK GREYS
• NOT LOTS OF YELLOW
• RESDENTIAL IMAGES

```html
<!DOCTYPE html>
<html lang="en">
<head>
<meta charset="utf-8">
<title>Brightwell Panes &amp; Stoneworks</title>
<link href="https://fonts.googleapis.com/css2?family=Open+Sans:wght@300;400;600;700;800&display=swap" rel="stylesheet">
<style>
:root{
  --yellow:#e6c31c;
  --text:#3d4448;
  --muted:#8a9094;
  --faint:#eeeff0;
  --teal:#1f4d58;
  --teal-deep:#16363f;
  --white:#ffffff;
}
*{margin:0;padding:0;box-sizing:border-box}
html,body{width:1200px;height:3564px;overflow:hidden;background:var(--white)}
body{position:relative;font-family:"Open Sans",Arial,sans-serif;color:var(--text)}
.abs{position:absolute}
.photo{position:absolute;overflow:hidden}
.watermark{position:absolute;font-weight:800;color:var(--faint);font-size:104px;letter-spacing:-2px;white-space:nowrap;line-height:1}
.eyebrow{font-size:13px;color:var(--muted)}
.link-more{font-size:12px;color:var(--text);font-weight:600}
.link-more b{color:var(--yellow)}
.vertical{position:absolute;writing-mode:vertical-rl;font-size:10px;letter-spacing:3px;text-transform:uppercase}

/* header */
.menu-icon{left:30px;top:30px}
.brand-mark{left:146px;top:18px;width:54px;height:54px;border-radius:50%;background:var(--yellow)}
.brand-sub{left:116px;top:86px;font-size:11px;font-weight:600;width:120px;text-align:center}
.site-title{right:40px;top:40px;text-align:right}
.site-title h1{font-size:22px;font-weight:700}
.site-title p{font-size:10px;color:var(--muted)}

/* social rail */
.follow{left:42px;top:430px;color:var(--muted)}
.social{left:44px;width:12px;height:12px;border-radius:50%;background:#9aa0a4}

/* hero */
.hero{left:100px;top:128px;width:1100px;height:512px;background:linear-gradient(160deg,#8fb3b8 0%,#4f6e70 45%,#2d3a36 75%,#5e6a3c 100%)}
.hero-copy{left:180px;top:492px;color:var(--white)}
.hero-copy small{font-size:14px;color:var(--yellow)}
.hero-copy strong{display:block;font-size:24px;font-weight:700}
.hero-copy span{font-size:14px}
.hero-count{left:1040px;top:570px;color:var(--white);font-size:14px}
.hero-count b{color:var(--yellow);font-size:28px}

/* welcome */
.welcome{right:124px;top:676px;text-align:right}
.welcome .eyebrow{font-size:15px}
.welcome h2{font-size:40px;font-weight:700;line-height:1.2}
.welcome p{font-size:12px;color:var(--muted);margin:4px 0 30px}

/* projects */
.proj-title{font-size:26px;font-weight:700;line-height:1.2}
.hotel-copy{left:664px;top:1080px}
.commercial-copy{right:640px;top:1420px;text-align:right}

/* band */
.panel{top:1632px;height:528px}
.panel-copy{position:absolute;left:40px;bottom:64px;color:var(--white)}
.panel-copy .eyebrow{color:#d9dde0}
.panel-copy h3{font-size:28px;font-weight:400;line-height:1.1}
.panel-copy h3 span{color:rgba(255,255,255,.6)}
.panel-copy .link-more{display:block;margin-top:16px;color:var(--yellow);font-weight:400}

/* testimonial */
.quote{left:150px;top:2270px;width:350px;text-align:right;font-size:13px;color:var(--muted);font-style:italic;line-height:1.7}
.quote-name{right:700px;top:2420px;font-size:12px}
.arrows{left:420px;top:2456px;font-size:16px}
.avatar{left:536px;top:2330px;width:128px;height:128px;border-radius:50%;background:radial-gradient(circle,#b49a84,#6c5a4e);border:6px solid var(--white);box-shadow:0 2px 10px rgba(0,0,0,.15)}
.clients{left:716px;top:2376px}

/* team */
.team-head{left:100px;top:2700px;width:140px;text-align:right}
.team-caption{position:absolute;left:22px;bottom:24px;color:var(--white);font-size:15px;font-weight:700}
.team-caption small{display:block;font-weight:400;font-size:11px}
.team-label{position:absolute;left:30px;bottom:40px;background:var(--yellow);color:var(--white);padding:6px 14px;font-size:13px;font-weight:700}

/* news */
.news{left:100px;top:3060px;width:1100px;height:340px;background:linear-gradient(120deg,var(--teal-deep),var(--teal) 60%,#2e6470)}
.news-head{left:140px;top:3086px;color:var(--white)}
.news-head .eyebrow{color:#c7d2d5}
.news-head h2{font-size:26px;font-weight:400}
.news-item{top:3176px;width:260px;color:var(--white)}
.news-item time{font-size:11px;color:#c7d2d5}
.news-item h4{font-size:15px;font-weight:700;line-height:1.35;margin:6px 0 24px}
.news-item .link-more{color:var(--white);font-weight:400}
.news-all{left:140px;top:3360px;color:var(--white);font-size:12px}
.news-all b{color:var(--yellow)}

/* footer */
.footer-links{left:100px;top:3500px;font-size:11px;color:var(--muted);display:flex;gap:28px}
.copyright{right:0;top:3494px;text-align:right;font-size:10px;color:var(--muted);line-height:1.5}
</style>
</head>
<body>

<header>
  <svg class="abs menu-icon" width="22" height="16" viewBox="0 0 22 16"><rect width="22" height="2" fill="#3d4448"/><rect y="7" width="22" height="2" fill="#3d4448"/><rect y="14" width="22" height="2" fill="#3d4448"/></svg>
  <div class="abs brand-mark"></div>
  <div class="abs brand-sub">Brightwell Panes &amp; Stoneworks</div>
  <div class="abs site-title">
    <h1>Brightwell Panes &amp; Stoneworks</h1>
    <p>Glass splashbacks and solid surfaces</p>
  </div>
</header>

<aside>
  <div class="vertical follow">Follow us</div>
  <div class="abs social" style="top:522px"></div>
  <div class="abs social" style="top:548px"></div>
  <div class="abs social" style="top:574px"></div>
  <div class="abs social" style="top:600px"></div>
  <div class="abs social" style="top:626px"></div>
</aside>

<section>
  <div class="photo hero" role="img" aria-label="Glass-walled boardroom with a long table and chairs overlooking the city"></div>
  <div class="abs hero-copy"><small>Brightwell</small><strong>Panes &amp; Stone</strong><span>Works</span></div>
  <div class="abs hero-count"><b>1</b> / 3</div>
  <svg class="abs" style="left:1040px;top:612px" width="60" height="3"><rect width="20" height="3" fill="#e6c31c"/><rect x="20" width="40" height="3" fill="rgba(255,255,255,.5)"/></svg>
</section>

<section class="welcome abs">
  <div class="eyebrow">Welcome to</div>
  <h2>Brightwell Panes &amp; Stoneworks</h2>
  <p>Crafted glass and stone surfaces for hotels and commercial spaces</p>
  <div class="link-more">Know More <b>→</b></div>
</section>

<section>
  <div class="watermark" style="left:600px;top:912px">BrightwellPS</div>
  <div class="watermark" style="left:100px;top:1252px">BrightwellPS</div>
  <div class="photo" style="left:100px;top:900px;width:500px;height:260px;background:linear-gradient(135deg,#ece6dc,#b9ab95 55%,#6e5f4c)" role="img" aria-label="Bright hotel lobby with glass walls and lounge seating"></div>
  <div class="abs hotel-copy">
    <div class="eyebrow">BrightwellPS</div>
    <div class="proj-title">Hotel Projects</div>
    <div class="link-more" style="margin-top:10px">View Projects <b>→</b></div>
  </div>
  <div class="photo" style="left:600px;top:1220px;width:500px;height:320px;background:linear-gradient(160deg,#8fb7d0,#6f7f8a 50%,#3f3a3a)" role="img" aria-label="Modern commercial tower with angled glass facade"></div>
  <div class="vertical" style="left:1112px;top:1260px;color:#8a9094">Commercial Projects</div>
  <div class="abs commercial-copy">
    <div class="eyebrow">BrightwellPS</div>
    <div class="proj-title">Commercial Projects</div>
    <div class="link-more" style="margin-top:10px">View Projects <b>→</b></div>
  </div>
</section>

<section>
  <div class="photo panel" style="left:100px;width:370px;background:linear-gradient(170deg,#6f8e95,#2e4a52)" role="img" aria-label="Curved glass office tower">
    <div class="panel-copy"><div class="eyebrow">BrightwellPS</div><h3>Commercial<br><span>Towers</span></h3><span class="link-more">View Projects →</span></div>
  </div>
  <div class="photo panel" style="left:470px;width:370px;background:linear-gradient(170deg,#d9dcdc,#9c9a92 55%,#6b6458)" role="img" aria-label="Atrium with spiral stairs in a holiday resort">
    <div class="panel-copy"><div class="eyebrow">BrightwellPS</div><h3>Holiday<br><span>Resorts</span></h3><span class="link-more">View Projects →</span></div>
  </div>
  <div class="photo panel" style="left:840px;width:360px;background:linear-gradient(170deg,#5c8f90,#2c4f52 60%,#6a6c2a)" role="img" aria-label="Residential complex with glass balconies">
    <div class="panel-copy"><div class="eyebrow">BrightwellPS</div><h3>Recidential<br><span>Complex</span></h3><span class="link-more">View Projects →</span></div>
  </div>
</section>

<section>
  <div class="watermark" style="left:620px;top:2262px">BrightwellPS</div>
  <p class="abs quote">" Every panel was fitted with real care and precision. The team kept the site tidy, met each deadline and the finished surfaces look superb in our new lobby and suites. "</p>
  <div class="abs quote-name">R. Calloway</div>
  <div class="abs arrows">‹ &nbsp; ›</div>
  <div class="abs avatar" role="img" aria-label="Client portrait"></div>
  <div class="abs clients"><div class="eyebrow">What</div><div class="proj-title" style="font-weight:400;font-size:22px">Our Clients<br>Says</div></div>
</section>

<section>
  <div class="watermark" style="left:100px;top:2640px">BPS</div>
  <div class="abs team-head">
    <div class="eyebrow">About</div>
    <div class="proj-title" style="font-size:22px">Our Team</div>
    <div class="link-more" style="margin-top:8px">View All <b>→</b></div>
  </div>
  <div class="photo" style="left:260px;top:2580px;width:280px;height:360px;background:linear-gradient(180deg,#cfcfcc,#8a7f72 60%,#3f4a3c)" role="img" aria-label="Team member portrait">
    <div class="team-caption">Lorem Ipsum<small>Director</small></div>
  </div>
  <div class="photo" style="left:540px;top:2620px;width:280px;height:300px;background:linear-gradient(180deg,#e9e2d8,#c4b09a)" role="img" aria-label="Team member portrait">
    <div class="team-label">Lorem Ipsum</div>
  </div>
  <div class="photo" style="left:820px;top:2620px;width:280px;height:300px;background:linear-gradient(180deg,#f0ece6,#bcb2a6)" role="img" aria-label="Team member portrait">
    <div class="team-label">Lorem Ipsum</div>
  </div>
  <div class="vertical" style="left:1108px;top:2640px;color:#8a9094">Meet our team</div>
</section>

<section>
  <div class="photo news" role="img" aria-label="Dark teal architectural glass structure"></div>
  <div class="abs news-head"><div class="eyebrow">Our</div><h2>Latest <b style="font-weight:700">News</b></h2></div>
  <div class="abs news-item" style="left:140px"><time>June 27 / 2018</time><h4>New hotel suite fitout with glass panels complete</h4><span class="link-more">Read More <b style="color:#e6c31c">→</b></span></div>
  <div class="abs news-item" style="left:460px"><time>June 27 / 2018</time><h4>Solid surface counters for a city office tower</h4><span class="link-more">Read More <b style="color:#e6c31c">→</b></span></div>
  <div class="abs news-item" style="left:780px"><time>June 27 / 2018</time><h4>Our team grows with two new project leads</h4><span class="link-more">Read More <b style="color:#e6c31c">→</b></span></div>
  <div class="abs news-all">View All News <b>→</b></div>
  <div class="vertical" style="left:1168px;top:3100px;color:#c7d2d5">Our latest news</div>
</section>

<footer>
  <div class="abs footer-links"><span>Privacy Policy</span><span>Terms</span><span>Contact</span></div>
  <div class="abs copyright">Copyright © 2018 Brightwell Panes &amp; Stoneworks<br>All rights reserved</div>
</footer>

</body>
</html>
```